NEW Website DESIGN for Glass & Solid Surfaces Company

Brand New website, contemporary, clean, visual (images), not busy. ATTACHED IS OUR LOG THAT YOU MUST USE.

The company is called Brightwell Panes & Stoneworks (BrightwellPS)
www.brightwellps.com
The website should be www.brightwellpns.com
one page for glass one page for solid surfaces www.brightwellpanesplashes.co.uk
www.brightwellstoneworkss.co.uk

Target Market(s)

Hotels, Commercial projects, Small focus on residential

Industry/Entity Type

Construction

Number of Pages Required

5+ page

Font styles to use
Sans Serif

Requirements
Must have
• COLOURS AS PER OUR LOGO - WHITE/YELLOW/GREY - WHITE BACK GROUND
• CLEAR SIMPLE NAVIGATION - MODER CLEAN CUT - DESIGN FEEL
• LATEST NAVIGATION FOR IMAGES and text to include per project details
• WORK/PROJECT AREA - NEWS AREA - TEAM AREA/ABOUT US/CONTACT US
• NEW PAGEwww.brightwellpanesplashes.co.uk - NEW PAGE www.brightwellstoneworkss.co.uk
• PLEASE COPY THIS TYPE OF TEMPALTE
• https://www.harlowmead.co.uk/project/grand-halls/
• MOBILE READY
• WORDPRESS
• MODERN IMAGES INCLUDING VELMARA KESTRIN AND GLASS PROJECTS
Nice to have
• NEW DESIGN MODER FRESH
• WEBSITES I LIKE THE TEMPLATE SHOULD BE LIKE THE WEBSITE BELOW
• https://www.harlowmead.co.uk/
Should not have
• NOT Old fashion template, not busy NAVIGATION
• NO BLACK
• NO DARK GREYS
• NOT LOTS OF YELLOW
• RESDENTIAL IMAGES

```html
<!DOCTYPE html>
<html lang="en">
<head>
<meta charset="utf-8">
<title>Brightwell Panes &amp; Stoneworks — Home</title>
<link href="https://fonts.googleapis.com/css2?family=Lato:wght@300;400;700&family=Tinos:wght@400&display=swap" rel="stylesheet">
<style>
:root{
  --stage:#e4e4e4;
  --white:#ffffff;
  --yellow:#d8d60c;
  --grey:#a6a6a6;
  --grey-dark:#8a8a8a;
  --grey-band:#b9b9b9;
  --text:#6f6f6f;
  --heading:#5e5e5e;
  --line:#dcdcdc;
}
*{box-sizing:border-box;margin:0;padding:0}
html,body{width:1200px;height:800px;overflow:hidden}
body{background:var(--stage);font-family:"Lato",sans-serif;color:var(--text);position:relative}
.page{position:absolute;left:465px;top:10px;width:540px;height:1560px;background:var(--white);transform:scale(.5);transform-origin:0 0;overflow:hidden}
.abs{position:absolute}
/* header */
.brand{left:14px;top:6px;display:flex;align-items:center;gap:4px;font-size:6px;color:var(--heading);font-weight:700}
.brand-dot{width:12px;height:12px;border-radius:50%;border:1.5px solid var(--grey)}
.nav{right:26px;top:11px;display:flex;gap:9px;font-size:5.5px;letter-spacing:.3px;color:var(--grey-dark)}
.nav .active{background:var(--yellow);color:var(--white);padding:1px 4px}
/* hero */
.social{left:22px;top:60px;display:flex;flex-direction:column;align-items:center;gap:8px}
.social .bar{width:1px;height:40px;background:var(--yellow)}
.social .ico{width:6px;height:6px;border-radius:50%;background:var(--grey)}
.hero{left:52px;top:30px;width:488px;height:185px;background:linear-gradient(90deg,#8c7a55,#c49a45 20%,#a0866a 40%,#d0a84a 60%,#8f7d63 80%,#c39a4c)}
.hero-copy{left:52px;top:88px;width:488px;text-align:center;color:var(--white);font-family:"Tinos",serif;font-size:11px;line-height:16px;letter-spacing:.3px}
.btn{display:inline-block;background:var(--yellow);color:var(--white);font-family:"Lato",sans-serif;font-size:5px;padding:3px 10px;letter-spacing:.4px}
/* headings */
.h2{font-size:10px;color:var(--heading);letter-spacing:.4px}
.h2::after{content:"";display:block;width:40px;height:1.5px;background:var(--yellow);margin-top:4px}
.h2.center{text-align:center;width:540px;left:0}
.h2.center::after{margin:4px auto 0}
.body{font-size:6.2px;line-height:10px;color:var(--text)}
.img{background:linear-gradient(160deg,#c9cfd6,#8d99a6)}
/* works */
.filters{left:0;width:540px;top:538px;display:flex;justify-content:center;gap:14px;font-size:5.5px;color:var(--grey-dark)}
.filters .active{background:var(--yellow);color:var(--white);padding:1px 5px}
/* team */
.member{width:118px;height:76px;background:linear-gradient(180deg,#9aa2a8,#6f7a80)}
.tag{width:70px;height:14px;background:var(--yellow);color:var(--white);font-size:4.5px;text-align:center;line-height:6px;padding-top:1px}
/* blog */
.post{width:148px}
.post .pic{height:82px}
.post .meta{font-size:4.5px;color:var(--grey);text-align:center;margin-top:5px}
.post .title{font-size:6px;color:var(--heading);text-align:center;margin-top:4px;font-weight:700}
.post .excerpt{font-size:4.5px;line-height:7px;color:var(--grey);text-align:center;margin-top:3px}
/* newsletter */
.news{left:0;top:1268px;width:540px;height:123px;background:linear-gradient(180deg,#c3c3c3,#a9a9a9)}
.news-title{left:0;width:540px;top:1296px;text-align:center;font-family:"Tinos",serif;color:var(--white);font-size:11px;letter-spacing:.4px}
.field{display:flex;align-items:center;gap:6px;font-size:5px;color:var(--white)}
.field span.box{display:block;width:150px;height:11px;background:#e6e6d2;border:1px solid var(--yellow)}
/* footer */
.footer{left:0;top:1391px;width:540px;height:169px;background:var(--grey)}
.fcol{color:var(--white);font-size:4.8px;line-height:8px}
.fcol h4{font-size:5.5px;font-weight:700;margin-bottom:6px;letter-spacing:.3px}
.fcol .y{display:inline-block;width:4px;height:4px;background:var(--yellow);border-radius:50%;margin-right:4px}
.copy{left:0;width:540px;top:1547px;text-align:center;font-size:4.5px;color:var(--white)}
</style>
</head>
<body>
<main class="page">
  <header>
    <div class="abs brand"><span class="brand-dot"></span>Brightwell Panes &amp; Stoneworks</div>
    <nav class="abs nav"><span class="active">HOME</span><span>PROJECTS</span><span>NEWS</span><span>ABOUT US</span><span>CONTACT</span></nav>
  </header>

  <section>
    <div class="abs social"><span class="bar"></span><span class="ico"></span><span class="ico"></span><span class="ico"></span><span class="ico"></span></div>
    <div class="abs hero" role="img" aria-label="Rippled water reflection of amber glass facade"></div>
    <div class="abs hero-copy">WE PROVIDE YOU<br>BEST QUALITY GLASS AND SOLID SURFACE<br><span class="btn" style="margin-top:5px">VIEW PROJECTS &nbsp;→</span></div>
  </section>

  <section>
    <h2 class="abs h2" style="left:37px;top:255px">ABOUT US</h2>
    <div class="abs body" style="left:37px;top:302px;width:230px">
      <p>Lorem Ipsum is simply dummy text of the printing and typesetting industry. Lorem Ipsum has been the industry's standard dummy text ever since the 1500s, when an unknown printer took a galley of type and scrambled it to make a type specimen book. It has survived not only five centuries, but also the leap into electronic typesetting, remaining essentially unchanged.</p>
      <p style="margin-top:8px">It is a long established fact that a reader will be distracted by the readable content of a page when looking at its layout. The point of using Lorem Ipsum is that it has a more-or-less normal distribution of letters, as opposed to using content here, making it look like readable English.</p>
    </div>
    <span class="abs btn" style="left:37px;top:458px">READ MORE</span>
    <div class="abs img" style="left:341px;top:296px;width:158px;height:171px;background:linear-gradient(180deg,#8a6a55,#c9c9cf 60%,#b6a8c0)" role="img" aria-label="Glass balustrade in a bright office corridor"></div>
  </section>

  <section>
    <h2 class="abs h2 center" style="top:506px">OUR RECENT WORKS</h2>
    <div class="abs filters"><span>ALL</span><span class="active">GLASS</span><span>SOLID</span></div>
    <div class="abs img" style="left:37px;top:556px;width:149px;height:166px" role="img" aria-label="Glass curtain wall project"></div>
    <div class="abs img" style="left:193px;top:556px;width:150px;height:166px;background:linear-gradient(160deg,#dfe4ea,#6d7b88)" role="img" aria-label="Framed glass facade grid"></div>
    <div class="abs img" style="left:351px;top:556px;width:149px;height:166px;background:linear-gradient(160deg,#eef2f6,#7d93ab)" role="img" aria-label="Corner of a glass building against the sky"></div>
    <span class="abs btn" style="left:238px;top:742px">VIEW MORE &nbsp;→</span>
  </section>

  <section>
    <h2 class="abs h2 center" style="top:790px">OUR TEAM</h2>
    <p class="abs body" style="left:70px;top:814px;width:400px;text-align:center;font-size:5.5px;line-height:8px">Lorem Ipsum is simply dummy text of the printing and typesetting industry. Lorem Ipsum has been the industry's standard dummy text ever since the 1500s, when an unknown printer took a galley of type and scrambled it to make a type specimen book. It has survived not only five centuries, but also the leap into electronic typesetting, remaining essentially unchanged.</p>
    <div class="abs member" style="left:72px;top:872px" role="img" aria-label="Portrait of team member"></div>
    <div class="abs member" style="left:213px;top:872px;background:linear-gradient(180deg,#c5d6e0,#8aa5b4)" role="img" aria-label="Portrait of team member"></div>
    <div class="abs member" style="left:346px;top:872px;background:linear-gradient(180deg,#b4b8bc,#6c7176)" role="img" aria-label="Portrait of team member"></div>
    <div class="abs tag" style="left:96px;top:956px">Team Name<br>Designer</div>
    <div class="abs tag" style="left:237px;top:956px">Team Name<br>Manager</div>
    <div class="abs tag" style="left:370px;top:956px">Team Name<br>Engineer</div>
  </section>

  <section>
    <p class="abs" style="left:0;width:540px;top:1019px;text-align:center;font-size:4.5px;color:var(--grey)">READ</p>
    <h2 class="abs h2 center" style="top:1030px">RECENT BLOG</h2>
    <article class="abs post" style="left:37px;top:1070px">
      <div class="pic" style="background:linear-gradient(160deg,#c8d0d4,#8f9ea4)" role="img" aria-label="Water drops on glass"></div>
      <p class="meta">Admin | 2018 | 12 Comments</p><p class="title">Blog1 title is here</p>
      <p class="excerpt">Lorem ipsum dolor sit amet, consectetur adipiscing elit, sed do eiusmod tempor incididunt ut labore et dolore magna aliqua enim ad minim veniam.</p>
    </article>
    <article class="abs post" style="left:195px;top:1070px">
      <div class="pic" style="background:linear-gradient(160deg,#6f7a70,#2f3530)" role="img" aria-label="Glass bottles in a row"></div>
      <p class="meta">Admin | 2018 | 12 Comments</p><p class="title">Blog2 title is here</p>
      <p class="excerpt">Lorem ipsum dolor sit amet, consectetur adipiscing elit, sed do eiusmod tempor incididunt ut labore et dolore magna aliqua enim ad minim veniam.</p>
    </article>
    <article class="abs post" style="left:353px;top:1070px">
      <div class="pic" style="background:linear-gradient(160deg,#5c6470,#262a33)" role="img" aria-label="Stacked wine glasses"></div>
      <p class="meta">Admin | 2018 | 12 Comments</p><p class="title">Blog3 title is here</p>
      <p class="excerpt">Lorem ipsum dolor sit amet, consectetur adipiscing elit, sed do eiusmod tempor incididunt ut labore et dolore magna aliqua enim ad minim veniam.</p>
    </article>
    <p class="abs" style="left:0;width:540px;top:1224px;text-align:center;font-size:4.5px;color:var(--grey)">Prev &nbsp; 1 2 &nbsp; <span style="color:var(--yellow)">Next</span></p>
  </section>

  <section>
    <div class="abs news" role="img" aria-label="Faded view of a glass tower"></div>
    <h3 class="abs news-title">SIGN UP FOR A NEWSLETTER</h3>
    <div class="abs field" style="left:60px;top:1340px">Name<span class="box"></span></div>
    <div class="abs field" style="left:262px;top:1340px">E-mail<span class="box"></span></div>
    <span class="abs btn" style="left:472px;top:1340px">SIGN UP</span>
  </section>

  <footer>
    <div class="abs footer"></div>
    <div class="abs fcol" style="left:30px;top:1406px;width:160px;text-align:center">
      <h4>ABOUT OUR COMPANY</h4>
      <p>Lorem Ipsum is simply dummy text of the printing and typesetting industry. Lorem Ipsum has been the industry's standard dummy text ever since the 1500s, when an unknown printer took a galley of type and scrambled it to make a type specimen book.</p>
      <h4 style="margin-top:6px">FOLLOW US</h4>
      <p><span class="y"></span><span class="y"></span><span class="y"></span><span class="y"></span></p>
    </div>
    <div class="abs fcol" style="left:232px;top:1406px;text-align:center">
      <h4>QUICK LINKS</h4><p>HOME<br>PROJECT<br>NEWS<br>ABOUT US<br>CONTACT</p>
    </div>
    <div class="abs fcol" style="left:318px;top:1406px">
      <h4>CONTACT US</h4>
      <p><span class="y"></span>+44 1632 960 418<br><span class="y"></span>www.brightwellps.com<br><span class="y"></span>info@brightwellps.com</p>
    </div>
    <div class="abs fcol" style="left:440px;top:1406px">
      <h4>LATEST BLOG</h4>
      <p>Blog 1 is here<br>25th June<br>Blog 2 is here<br>25th June<br>Blog 3 is here<br>25th June<br>Blog 4 is here<br>25th June</p>
    </div>
    <p class="abs copy">Copyright 2018 • All Right Reserved</p>
  </footer>
</main>
</body>
</html>
```